New website

We ned to create a new website that reflects more who we are. We are delivering exclusive premium products to our customers and the current website does not reflect our products at all.
We believe in less is more and need a webpage that is clean yet professional and exclusive.

Target Market(s)

Dentistry

Industry/Entity Type

Dental

Number of Pages Required

5+ page

Font styles to use
Sans Serif

Colors

Designer to choose colors to be used in the design.

Requirements
Must have
• Picture gallery
• Nice structure
• Clean layout
Nice to have
• Light fonts
Should not have
• Any italic font styles

```html
<!DOCTYPE html>
<html lang="en">
<head>
<meta charset="utf-8">
<title>Lumadent – Professional Dental Care</title>
<link rel="stylesheet" href="https://fonts.googleapis.com/css2?family=Open+Sans:wght@300;400;600;700&display=swap">
<style>
:root{
  --blue:#1d6db3;
  --blue-dark:#155a96;
  --blue-deep:#0f4c80;
  --red:#e2323f;
  --ink:#3a3f47;
  --muted:#8a9099;
  --line:#e3e6ea;
  --soft:#f3f4f6;
  --white:#ffffff;
}
*{box-sizing:border-box;margin:0;padding:0}
html,body{width:1200px;height:2400px;overflow:hidden}
body{font-family:"Open Sans",Arial,sans-serif;color:var(--ink);background:var(--white);font-size:13px;line-height:1.55}
a{color:inherit;text-decoration:none}
.btn{display:inline-block;font-size:11px;font-weight:600;letter-spacing:.06em;text-transform:uppercase;padding:9px 20px;border-radius:2px;color:var(--white)}
.btn-red{background:var(--red)}
.btn-blue{background:var(--blue)}
.btn-outline{border:1px solid var(--white);color:var(--white)}
.section-title{font-weight:300;font-size:28px;letter-spacing:.02em;text-transform:uppercase}

/* top bar */
.topbar{height:32px;background:var(--blue);color:#dce9f5;font-size:11px;display:flex;align-items:center;justify-content:space-between;padding:0 40px}
.topbar .links span{margin-left:16px}
.topbar .lang{background:var(--red);color:#fff;padding:3px 10px;margin-left:16px}

/* header */
.header{height:56px;display:flex;align-items:center;padding:0 40px 0 70px}
.brand{display:flex;align-items:center;gap:10px;font-weight:700;font-size:16px;letter-spacing:.12em;color:var(--blue)}
.brand i{width:18px;height:18px;background:var(--red);display:block}
.nav{display:flex;margin-left:auto;gap:26px;font-size:11px;font-weight:600;text-transform:uppercase;letter-spacing:.05em;color:var(--muted)}
.nav .active{color:var(--blue);border-bottom:2px solid var(--blue);padding-bottom:4px}
.header .btn{margin-left:34px}

/* hero */
.hero{position:relative;height:372px;background:linear-gradient(100deg,#cfe0ee 0%,#9fc2df 40%,#5d8fbd 70%,#e7eef4 100%)}
.hero-card{position:absolute;left:240px;top:40px;width:300px;background:var(--blue);color:#fff;padding:24px 22px 22px}
.hero-card h1{font-size:26px;font-weight:600;line-height:1.1;text-transform:uppercase}
.hero-card h1 span{font-weight:300;display:block}
.hero-card p{font-size:11px;margin:10px 0 14px;color:#d7e7f6}
.hours{position:absolute;left:240px;top:222px;width:300px;background:#fff;padding:16px 22px;box-shadow:0 4px 14px rgba(0,0,0,.12);font-size:11px}
.hours h3{color:var(--red);font-size:13px;font-weight:700;text-transform:uppercase;margin-bottom:8px}
.hours li{list-style:none;display:flex;justify-content:space-between;border-bottom:1px solid var(--line);padding:4px 0}
.hours li b{color:var(--blue);font-weight:600}

/* about */
.about{height:502px;background:linear-gradient(180deg,#f7f8fa,#eef0f3);position:relative}
.about-photo{position:absolute;left:160px;top:0;width:400px;height:502px;background:linear-gradient(180deg,#e9ecef,#d6dbe0)}
.about-body{position:absolute;left:640px;top:98px;width:460px}
.about-body h2{color:var(--blue);font-weight:300;font-size:26px;text-transform:uppercase}
.about-body p{font-size:11px;color:var(--muted);margin-top:8px}
.features{display:grid;grid-template-columns:1fr 1fr;gap:28px 20px;margin-top:34px}
.feature{display:flex;align-items:center;gap:12px;font-size:11px;font-weight:600;text-transform:uppercase;color:var(--ink)}
.feature svg{width:34px;height:34px;flex:none}

/* products */
.products{height:380px;padding-top:78px;position:relative}
.products .section-title{margin-left:220px}
.pager{position:absolute;right:220px;top:86px;display:flex;gap:4px}
.pager i{width:16px;height:16px;border-radius:50%;border:1px solid var(--line);display:block}
.pager i.on{background:var(--blue);border-color:var(--blue)}
.cards{display:flex;gap:16px;margin:34px 0 0 220px}
.card{width:178px;text-align:center;font-size:10px;color:var(--muted)}
.card .img{height:108px;position:relative}
.card .tag{position:absolute;left:50%;bottom:-12px;transform:translateX(-50%);width:24px;height:24px;border-radius:50%;background:var(--red);border:2px solid #fff}
.card h4{margin-top:20px;font-size:11px;font-weight:600;color:var(--ink);text-transform:uppercase}
.card p{margin:6px 6px 10px;line-height:1.4}
.card .btn{padding:6px 16px;font-size:9px}

/* gallery */
.gallery{height:420px;position:relative;background:linear-gradient(90deg,#5b6068,#878c93 50%,#6d737b);color:#fff}
.gallery .section-title{position:absolute;left:220px;top:48px}
.gallery .pager{top:56px}
.gallery .pager i{border-color:#fff}
.shots{position:absolute;left:240px;top:100px;display:flex;gap:12px}
.shot{width:232px;height:160px;position:relative;background:#fff;padding:4px}
.shot .img{height:126px}
.shot .labels{display:flex;justify-content:space-between;align-items:center;font-size:9px;font-weight:700;color:var(--ink);padding:6px 10px 0;text-transform:uppercase}
.shot .mid{position:absolute;left:50%;top:122px;transform:translateX(-50%);width:28px;height:28px;border-radius:50%;background:var(--red);border:2px solid #fff}
.gallery .btn{position:absolute;left:50%;top:352px;transform:translateX(-50%)}

/* testimonials */
.reviews{height:340px;position:relative;padding-top:58px}
.reviews .section-title{margin-left:220px;color:var(--blue)}
.quotes{display:flex;gap:30px;margin:30px 0 0 220px}
.quote{width:365px;border:1px solid var(--line);padding:22px 22px 18px 72px;position:relative;font-size:10px;color:var(--muted)}
.quote .mark{position:absolute;left:22px;top:10px;font-size:60px;line-height:1;color:var(--blue);font-weight:700}
.quote a{display:block;margin-top:10px;color:var(--red);font-weight:600;text-transform:uppercase;font-size:9px}
.reviews .btn{position:absolute;left:50%;top:272px;transform:translateX(-50%)}

/* footer */
.footer{height:300px;background:var(--blue);color:#d8e6f3;position:relative;font-size:11px}
.contacts{display:flex;justify-content:center;gap:100px;padding-top:30px}
.contact{display:flex;gap:14px;width:200px}
.contact svg{width:40px;height:40px;flex:none}
.contact h5,.col h5{color:#fff;font-size:12px;font-weight:600;text-transform:uppercase;margin-bottom:4px}
.divider{margin:24px 220px 0;border-top:1px solid rgba(255,255,255,.2)}
.cols{display:flex;gap:50px;margin:20px 0 0 220px}
.col{width:160px}
.col ul{list-style:none;display:grid;grid-template-columns:1fr 1fr;gap:2px 10px}
.col .field{background:#fff;color:var(--muted);padding:6px 10px;font-size:10px;margin-top:4px}
.socials{display:flex;gap:6px;margin-top:60px;justify-content:flex-end}
.socials i{width:20px;height:20px;border-radius:50%;background:#fff;display:block;opacity:.9}
.copyright{position:absolute;left:0;right:0;bottom:0;height:34px;background:var(--blue-deep);display:flex;align-items:center;padding-left:220px;gap:40px;font-size:10px}
</style>
</head>
<body>

<div class="topbar">
  <span>To book a call: +00 555 010 220</span>
  <span class="links"><span>Home</span><span>Testimonials</span><span>Contact</span><span class="lang">Select Language</span></span>
</div>

<header class="header">
  <div class="brand"><i></i>LUMADENT</div>
  <nav class="nav">
    <a class="active">Products</a><a>Special Service</a><a>Smile Gallery</a><a>Contact</a><a>Where We Are</a>
  </nav>
  <a class="btn btn-red">Book an Appointment</a>
</header>

<section class="hero" role="img" aria-label="Dentist treating a patient in a bright clinic">
  <div class="hero-card">
    <h1>Professional<span>Dental Care</span></h1>
    <p>Our specialists bring premium care and modern materials to every smile we treat.</p>
    <a class="btn btn-outline">Book an Appointment</a>
  </div>
  <div class="hours">
    <h3>Working Time</h3>
    <ul>
      <li>Monday–Friday <b>08:00 – 18:00</b></li>
      <li>Saturday <b>09:00 – 14:00</b></li>
      <li>Sunday <b>Closed</b></li>
    </ul>
  </div>
</section>

<section class="about">
  <div class="about-photo" role="img" aria-label="Smiling dental assistant in a white uniform"></div>
  <div class="about-body">
    <h2>Who designed this smile?</h2>
    <p>Our team combines years of clinical experience with exclusive premium products. Every treatment is planned with care so that each patient leaves with a confident, natural smile that lasts.</p>
    <div class="features">
      <div class="feature"><svg viewBox="0 0 34 34" fill="none" stroke="#e2323f" stroke-width="1.6"><rect x="6" y="8" width="22" height="18" rx="2"/><path d="M6 13h22M12 5v6M22 5v6"/></svg>Free Consultation</div>
      <div class="feature"><svg viewBox="0 0 34 34" fill="none" stroke="#e2323f" stroke-width="1.6"><circle cx="17" cy="12" r="6"/><path d="M6 29c1-7 6-10 11-10s10 3 11 10"/></svg>Qualified Doctors</div>
      <div class="feature"><svg viewBox="0 0 34 34" fill="none" stroke="#e2323f" stroke-width="1.6"><circle cx="17" cy="17" r="11"/><path d="M17 10v14M13 13h6a2.5 2.5 0 010 5h-4a2.5 2.5 0 000 5h6"/></svg>Affordable Prices</div>
      <div class="feature"><svg viewBox="0 0 34 34" fill="none" stroke="#e2323f" stroke-width="1.6"><path d="M8 17l6 6 12-12"/><circle cx="17" cy="17" r="12"/></svg>Professional Staff</div>
    </div>
  </div>
</section>

<section class="products">
  <h2 class="section-title">Our Products</h2>
  <div class="pager"><i></i><i class="on"></i></div>
  <div class="cards">
    <div class="card"><div class="img" role="img" aria-label="Close-up of veneers on a smile" style="background:linear-gradient(135deg,#e89aa8,#c45a6d)"><span class="tag"></span></div><h4>Veneers</h4><p>Thin shells shaped to give teeth a bright, even look.</p><a class="btn btn-blue">Read More</a></div>
    <div class="card"><div class="img" role="img" aria-label="Close-up of white teeth" style="background:linear-gradient(135deg,#f1d3cf,#d98b8b)"><span class="tag"></span></div><h4>Crown Bridge</h4><p>Durable restorations that bring back strength and form.</p><a class="btn btn-blue">Read More</a></div>
    <div class="card"><div class="img" role="img" aria-label="Dental tools on a tray" style="background:linear-gradient(135deg,#8d949c,#4e555d)"><span class="tag"></span></div><h4>Dentures</h4><p>Comfortable fitted sets made with premium materials.</p><a class="btn btn-blue">Read More</a></div>
    <div class="card"><div class="img" role="img" aria-label="Dental implant model" style="background:linear-gradient(135deg,#f0c6c6,#c97a84)"><span class="tag"></span></div><h4>Implants</h4><p>Stable long-term replacements for missing teeth.</p><a class="btn btn-blue">Read More</a></div>
  </div>
</section>

<section class="gallery" role="img" aria-label="Blurred dental clinic background">
  <h2 class="section-title">Smile Gallery</h2>
  <div class="pager"><i></i><i class="on"></i></div>
  <div class="shots">
    <div class="shot"><div class="img" role="img" aria-label="Smile before and after whitening" style="background:linear-gradient(90deg,#c77a7a,#e9c9c2)"></div><div class="labels"><span>Before</span><span>After</span></div><span class="mid"></span></div>
    <div class="shot"><div class="img" role="img" aria-label="Smile before and after veneers" style="background:linear-gradient(90deg,#d89a9a,#f2dcd6)"></div><div class="labels"><span>Before</span><span>After</span></div><span class="mid"></span></div>
    <div class="shot"><div class="img" role="img" aria-label="Teeth before and after restoration" style="background:linear-gradient(90deg,#b86464,#e8c0b2)"></div><div class="labels"><span>Before</span><span>After</span></div><span class="mid"></span></div>
  </div>
  <a class="btn btn-red">View Full Gallery</a>
</section>

<section class="reviews">
  <h2 class="section-title">Patients Shared Experience</h2>
  <div class="quotes">
    <div class="quote"><span class="mark">“</span>The whole team made me feel at ease from the first visit. My new smile looks natural and the treatment was quick, calm and clearly explained at every single step of the way.<a>Anna Reed</a></div>
    <div class="quote"><span class="mark">“</span>I was nervous about implants, but the doctors planned everything carefully. The result feels like my own teeth and I would happily recommend this clinic to friends and family.<a>Mark Doyle</a></div>
  </div>
  <a class="btn btn-red">Read All Comments</a>
</section>

<footer class="footer">
  <div class="contacts">
    <div class="contact"><svg viewBox="0 0 40 40" fill="none" stroke="#fff" stroke-width="1.6"><path d="M20 34s-10-10-10-17a10 10 0 0120 0c0 7-10 17-10 17z"/><circle cx="20" cy="17" r="3.5"/></svg><div><h5>Our Location</h5>12 Harbour Lane<br>1000 Northfield</div></div>
    <div class="contact"><svg viewBox="0 0 40 40" fill="none" stroke="#fff" stroke-width="1.6"><path d="M12 8h5l2 7-3 2a16 16 0 007 7l2-3 7 2v5a2 2 0 01-2 2A22 22 0 0110 10a2 2 0 012-2z"/></svg><div><h5>Call Us</h5>+00 555 010 220<br>Get directions by phone</div></div>
    <div class="contact"><svg viewBox="0 0 40 40" fill="none" stroke="#fff" stroke-width="1.6"><rect x="7" y="11" width="26" height="18" rx="1"/><path d="M7 12l13 10 13-10"/></svg><div><h5>Email Us</h5>hello@lumadent.example<br>Reply within one day</div></div>
  </div>
  <div class="divider"></div>
  <div class="cols">
    <div class="col"><h5>Products</h5><ul><li>Veneers</li><li>Whitening</li><li>Crown Bridge</li><li>Implants</li><li>Dentures</li><li>Braces</li></ul></div>
    <div class="col"><h5>Search on Site</h5><div class="field">Type your search</div></div>
    <div class="col" style="width:220px"><h5>Meet Our Doctors</h5><div class="field">Select a specialist</div><div class="socials"><i></i><i></i><i></i></div></div>
  </div>
  <div class="copyright"><span>Copyright © 2025 Lumadent. All rights reserved.</span><span>Privacy Policy</span><span>Terms of Use</span></div>
</footer>

</body>
</html>
```